Business Card Design using new logo

As much as we'd like to think that treating everyone equally is the best strategy for fairness, the reality is that the differences in the lives of women and men have to be taken into account to ensure that organizations, programs, services, and yes, even public policy treat women and men in ways that achieve gender equity.

That's where ParityLumen - fairness metrics insight comes in. Using the data-driven tools of gender analysis, our organization can help anyone determine if gender equity is being achieved - in businesses and organizations, in the planning and implementation of programs and services, and in the development and enforcement of public policy.
Updates

Apologies for the delay - have not had time to finalize the decision.  Should be early this week - probably Tuesday.

Industry/Entity Type

Business

Requirements
Must have
• New Logo for ParityLumen
• Logo plus words "Fairness Metrics Insight"

```html
<!DOCTYPE html>
<html lang="en">
<head>
<meta charset="utf-8">
<title>ParityLumen Business Card</title>
<link rel="stylesheet" href="https://fonts.googleapis.com/css2?family=Ubuntu:wght@400;500&display=swap">
<style>
  :root {
    --backdrop: #e4e2df;
    --card-white: #ffffff;
    --card-front: #f4f4f4;
    --ink: #1d1d1d;
    --muted: #3a3a3a;
    --orange: #ef8a1f;
    --band: #161616;
    --ghost: #e6e6e6;
  }
  * { margin: 0; padding: 0; box-sizing: border-box; }
  html, body { width: 1200px; height: 951px; overflow: hidden; }
  body {
    background: var(--backdrop);
    position: relative;
    font-family: "Ubuntu", sans-serif;
    color: var(--ink);
  }
  .card {
    position: absolute;
    border-radius: 22px;
    overflow: hidden;
    box-shadow: 0 10px 28px rgba(0,0,0,0.25);
  }
  /* Front */
  .card-front {
    left: 70px; top: 70px;
    width: 600px; height: 360px;
    background: linear-gradient(160deg, var(--card-white), var(--card-front));
  }
  .front-ghost {
    position: absolute;
    left: 230px; top: 20px;
    width: 300px; height: 300px;
    border-radius: 50%;
    border: 34px solid var(--ghost);
  }
  .front-brand {
    position: absolute;
    left: 90px; top: 126px;
    display: flex; align-items: center; gap: 18px;
  }
  .brand-dot {
    width: 56px; height: 56px;
    border-radius: 50%;
    background: var(--orange);
  }
  .front-brand .brand-name { font-size: 62px; font-weight: 500; color: var(--ink); letter-spacing: -0.5px; }
  .front-tagline {
    position: absolute;
    left: 218px; top: 226px;
    font-size: 20px; color: var(--muted); letter-spacing: 0.6px;
  }
  /* Back */
  .card-back {
    left: 470px; top: 480px;
    width: 630px; height: 370px;
    background: var(--card-white);
  }
  .back-bands { position: absolute; inset: 0; }
  .back-brand {
    position: absolute;
    left: 34px; top: 58px;
    display: flex; align-items: center; gap: 12px;
  }
  .back-brand .brand-dot { width: 36px; height: 36px; }
  .back-brand .brand-name { font-size: 38px; font-weight: 500; color: var(--ink); }
  .holder {
    position: absolute;
    left: 430px; top: 62px;
  }
  .holder-name { font-size: 20px; color: var(--ink); }
  .holder-role { font-size: 15px; color: var(--orange); margin-top: 2px; }
  .address {
    position: absolute;
    left: 40px; top: 262px;
    color: #fff; font-size: 19px; line-height: 1.35;
    display: flex; gap: 10px;
  }
  .contact-list {
    position: absolute;
    left: 376px; top: 242px;
    list-style: none;
    color: #fff; font-size: 19px; line-height: 1.38;
  }
  .contact-list li { display: flex; align-items: center; gap: 12px; }
  .icon { width: 17px; height: 17px; flex: none; }
</style>
</head>
<body>

  <section class="card card-front">
    <div class="front-ghost"></div>
    <div class="front-brand">
      <span class="brand-dot"></span>
      <span class="brand-name">ParityLumen</span>
    </div>
    <p class="front-tagline">Fairness Metrics Insight</p>
  </section>

  <section class="card card-back">
    <svg class="back-bands" viewBox="0 0 630 370" preserveAspectRatio="none" aria-hidden="true">
      <path d="M0 160 C170 110 390 125 630 170 L630 370 L0 370 Z" fill="var(--band)"/>
      <path d="M0 180 C190 140 400 160 630 190 L630 370 L0 370 Z" fill="var(--orange)"/>
    </svg>

    <div class="back-brand">
      <span class="brand-dot"></span>
      <span class="brand-name">ParityLumen</span>
    </div>
    <div class="holder">
      <p class="holder-name">Marcus Ellery</p>
      <p class="holder-role">director</p>
    </div>

    <div class="address">
      <svg class="icon" viewBox="0 0 16 16" aria-hidden="true"><path d="M8 1 L1 8 H3 V15 H6.5 V10.5 H9.5 V15 H13 V8 H15 Z" fill="#fff"/></svg>
      <p>4100 Alder Vale Rd<br>Brinton, TX 78110</p>
    </div>

    <ul class="contact-list">
      <li>
        <svg class="icon" viewBox="0 0 16 16" aria-hidden="true"><path d="M4 1 L6.5 4.5 L5 6.5 C6 8.5 7.5 10 9.5 11 L11.5 9.5 L15 12 L13 15 C7 14 2 9 1 3 Z" fill="#fff"/></svg>
        555-014-2270
      </li>
      <li>
        <svg class="icon" viewBox="0 0 16 16" aria-hidden="true"><rect x="1" y="6" width="14" height="8" rx="1.5" fill="#fff"/><rect x="4" y="2" width="8" height="5" fill="#fff"/></svg>
        555-014-2271
      </li>
      <li>
        <svg class="icon" viewBox="0 0 16 16" aria-hidden="true"><rect x="1" y="3" width="14" height="10" rx="1.5" fill="#fff"/><path d="M1.5 4 L8 9 L14.5 4" stroke="var(--orange)" stroke-width="1.4" fill="none"/></svg>
        info@paritylumen.com
      </li>
      <li>
        <svg class="icon" viewBox="0 0 16 16" aria-hidden="true"><circle cx="8" cy="8" r="7" fill="#fff"/></svg>
        www.paritylumen.com
      </li>
    </ul>
  </section>

</body>
</html>
```